vermalo web design

- Company / Site Description
We are developing a website that will allow anyone in Europe to find in one click, cultural things to do (Exhibition, Museum, Monument, Zoo, Aquarium, Archaeological site…) with friends or family, and to organize the visit (book a ticket / a private visit, book a restaurant nearby…).

Examples
1. You're in London with your girlfriend, it's saturday 10 am, you have two hours to spend and you want to see an exhibition. We provide you in one click all the exhibition matching your location / time and date.

2. You're in Berlin with some friends, it's thursday night you want to go out, but you don't know what to do. We provide you a list of experience, you can select for instance "I want to be on top of the world", and we show you a list of venues matching the selected experience / date / time /location of your request.

- Brand name : Vermalo
- Activity : Cultural Leisure, cultural entertainment

- Target audience
Broad target will be between 20 and 55. Core target will be between 25 and 40. Most likely to live in a city and in Europe.

- Behaviours and preferences
Our user is under time constraint (few minutes to find and choose his visit), idea constraint (is not sure about what to do and see) and money constraint.
He wants to have an easy to use website, not cluttered with information, focussed on added value information. He wants to have a website which is modern, fun and elegant that he will deem as professional and trustworthy.

- Our expectations (Do’s and Don’t)
We want to move away from traditional design. We want some OUT OF THE BOX design. Think of a website design that will look like an app design.
We want to make an awesome / extra ordinary /remember-able design. The design must be so cool, that the user wants to come back to the site. In two words: THINK EXTRAORDINARY.
You can use photos to help the user understand functions. If you use photo, use creative commons license photo.
Avoid black colors

- Functional Requirements
We need Four pages:
1. Home Page (desktop and mobile version): it’s both the homepage and the assistant page. This page will allow the user to find in one click his visit (please refer to the pdf file Assistant home page). The page must be self-explanatory for a first time user.
2. Assistant result page (desktop version): it’s the page that display the results found by the assistant based on the criteria search (please refer to the pdf file mockup - Assistant result page)
3. Site / Event page (desktop version): it’s the page that display each result information (please refer to the pdf file mockup – Event / Site Page)
The pdf files list all the elements include in each page + gives you a mockup of each page (just to put in perspective the element required). You are completely free about the design.
We don’t have the logo yet. Use a dummy logo for your page design.
The selected winner can expect to work with us immediately after the contest and on a on a regular basis later on.

- Technical Requirements
No Flash
For the winner, we will manage the CSS you will just need to provide :
. One PSD file containing all the pages
. Inside the PSD file we want for each page two groups: the first group will embed the desktop design, the second group will embed the responsive mobile design (Home Page only).
In total there should be 4 groups inside the PSD file (3 desktop groups, 1 mobile group).
Each group must contain all the elements specified in the pdf file

Website we like
http://demo.plandorix.example/?theme=Velunt
http://rosabel.quintorhub.example/#home
http://blogsite.fenk.daltoroute.example/2/
http://demo.plandorix.example/?theme=Mosaru
http://www.quarnivo.example/themes/lumbe/
http://gridmarket.example/item/tav-responsive-photography-blog-theme/full_screen_preview/8146027
http://items.zkvortel.example/?product=example
http://uk.harnoway.example

Reason: Due to the request of several designers, we have agreed to add 7 additional days to the contest deadline. Thank you. The vermalo team

Reason: We still need to collect all the votes. Sorry for the delay.

Reason: Hello, We extend the contest deadline, in order to collect all the votes from the poll. We should have everything finalized by sunday. Thank you vermalo team

```html
<!DOCTYPE html>
<html lang="en">
<head>
<meta charset="utf-8">
<title>Vermalo – My Assistant results</title>
<link rel="stylesheet" href="https://fonts.googleapis.com/css2?family=Questrial&family=Didact+Gothic&display=swap">
<style>
:root{
  --page:#e6e6e6;
  --blue:#1a9cf0;
  --ink:#2a2a2a;
  --grey-text:#7d7d7d;
  --slate:#8f8a86;
  --slate-dark:#7c7773;
  --footer:#efe9e2;
  --heart:#6c6c6c;
  --mint:#1ff2a6;
  --cyan:#14eeff;
  --crimson:#ff2352;
  --sun:#ffdc22;
  --coral:#ff6150;
  --sky:#1aa2f2;
  --apricot:#f2a252;
  --magenta:#be1fb2;
  --rose:#f2125c;
  --tangerine:#f06212;
  --violet:#b242d2;
  --lemon:#f8e032;
}
*{box-sizing:border-box;margin:0;padding:0}
html,body{width:1200px;height:998px;overflow:hidden}
body{background:var(--page);font-family:"Questrial",sans-serif;color:var(--ink);position:relative}
.app{position:absolute;left:0;top:160px;width:1200px;height:678px;overflow:hidden;
  background:
    radial-gradient(ellipse 380px 160px at 180px 580px,rgba(244,150,160,.45),transparent 70%),
    radial-gradient(ellipse 420px 200px at 1040px 420px,rgba(250,205,150,.55),transparent 70%),
    radial-gradient(ellipse 300px 140px at 720px 620px,rgba(240,160,160,.35),transparent 70%),
    radial-gradient(ellipse 360px 120px at 500px 320px,rgba(250,220,190,.45),transparent 70%),
    linear-gradient(180deg,#ececea 0%,#f3e8de 45%,#f2d6cf 100%);}
.abs{position:absolute}
.divider{left:406px;top:0;width:1px;height:678px;background:rgba(26,156,240,.25)}
.nav-rule{left:131px;top:91px;width:252px;height:1px;background:rgba(26,156,240,.45)}
.home-icon{left:154px;top:44px}
.nav{left:214px;top:47px;font-size:11px;color:var(--blue);display:flex;gap:14px}
.nav .active{font-weight:700;font-family:"Didact Gothic",sans-serif;font-weight:bold}
.weather{left:423px;top:14px;width:76px;height:76px;border:1px solid var(--blue);border-radius:50%;
  text-align:center;color:var(--blue);font-size:9px;line-height:10px;padding-top:14px}
.weather svg{display:block;margin:0 auto 2px}
.search{left:795px;top:77px;width:156px;height:16px;border:1px solid var(--blue);border-radius:8px;
  font-size:9px;color:#444;padding:2px 10px;background:rgba(255,255,255,.35)}
.gear{left:952px;top:12px}
.avatar{left:961px;top:15px;width:76px;height:76px;border-radius:50%;
  background:radial-gradient(circle at 50% 40%,#8a8a8a,#3a3a3a 60%,#1e1e1e);}
.greeting{left:961px;top:94px;width:76px;text-align:center;color:var(--blue);font-size:10px;line-height:11px}
.greeting b{font-family:"Didact Gothic",sans-serif}
.section-title{font-size:20px;color:var(--grey-text);font-weight:400}
.tile{position:absolute;font-size:14px;color:var(--ink);display:flex;align-items:center;justify-content:center}
.tile .remove{position:absolute;top:3px;right:5px;width:18px;height:18px;border:2.5px solid #111;border-radius:50%;
  font-size:8px;line-height:13px;text-align:center;color:#333}
.date{left:131px;top:440px;width:217px;height:22px;background:var(--slate);color:#fff;font-size:14px;padding:2px 7px}
.edit{left:349px;top:440px;width:49px;height:22px;border:1px solid #fff;color:#fff;font-size:9px;text-align:center;line-height:20px;font-family:"Didact Gothic",sans-serif;font-weight:bold;letter-spacing:.5px;background:rgba(255,255,255,.1)}
.time{left:131px;top:463px;width:85px;height:39px;background:var(--slate-dark);color:#fff;font-size:20px;text-align:center;line-height:39px}
.city{left:217px;top:463px;width:85px;height:39px;background:var(--slate);color:#fff;text-align:center;padding-top:5px;font-size:14px;line-height:14px;font-family:"Didact Gothic",sans-serif;font-weight:bold}
.city small{display:block;font-size:9px;font-weight:400}
.back{left:133px;top:536px;width:74px;height:74px;border:3px solid var(--blue);border-radius:50%;color:var(--blue);
  font-size:17px;text-align:center;line-height:68px;font-family:"Didact Gothic",sans-serif;font-weight:bold;letter-spacing:1px}
.card{position:absolute;width:252px;height:95px}
.card .body{position:absolute;left:0;top:0;width:153px;height:76px;padding:6px 5px}
.card h3{font-weight:400;font-size:13px;line-height:13px;color:#333;margin-bottom:4px}
.card p{font-size:8px;line-height:10px;color:#111;font-family:"Didact Gothic",sans-serif;font-weight:bold}
.card .photo{position:absolute;left:153px;top:0;width:99px;height:76px}
.card .meta{position:absolute;left:0;top:76px;width:252px;height:19px;background:var(--footer);font-size:8.5px;color:#666;padding:4px 5px}
.card .meta svg{position:absolute;right:6px;top:3px}
.photo-hall{background:linear-gradient(180deg,#2a2a2a,#bdbdbd 55%,#e8e8e8)}
.photo-museum{background:linear-gradient(180deg,#5a5a5a,#9a9a9a 50%,#444)}
.photo-dome{background:linear-gradient(180deg,#3c6fc0 0%,#6a96d8 40%,#d88a3a 62%,#6a3a20 100%)}
.photo-park{background:linear-gradient(180deg,#c8c8c8,#6a6a6a 50%,#3a3a3a)}
.rail{left:973px;top:147px;width:1px;height:522px;background:rgba(26,156,240,.35)}
.rail-cap{left:966px;top:147px;width:8px;height:1px;background:rgba(26,156,240,.35)}
.rail-arrow{left:973px;top:402px}
</style>
</head>
<body>
<main class="app">
  <div class="abs divider"></div>

  <svg class="abs home-icon" width="28" height="26" viewBox="0 0 28 26" aria-label="Home">
    <path d="M14 2 L26 13 H22 V24 H17 V17 H11 V24 H6 V13 H2 Z" fill="var(--blue)"/>
    <rect x="19" y="3" width="3" height="6" fill="var(--blue)"/>
  </svg>
  <nav class="abs nav"><span>Favourites</span><span>|</span><span class="active">My Assistant</span></nav>
  <div class="abs nav-rule"></div>

  <div class="abs weather">
    <svg width="26" height="20" viewBox="0 0 26 20" aria-hidden="true">
      <path d="M7 13 a5 5 0 0 1 1-10 a6 6 0 0 1 11 2 a4 4 0 0 1 0 8 Z" fill="none" stroke="var(--blue)" stroke-width="1.5"/>
      <path d="M2 6 H8 M1 9 H6" stroke="var(--blue)" stroke-width="1.2"/>
      <path d="M10 15 v3 M14 15 v3 M18 15 v3" stroke="var(--blue)" stroke-width="1.2"/>
    </svg>
    <b>8 °c</b><br>Rain, Wind
  </div>

  <div class="abs search">Search...</div>
  <svg class="abs gear" width="16" height="16" viewBox="0 0 16 16" aria-label="Settings">
    <circle cx="8" cy="8" r="5" fill="none" stroke="var(--blue)" stroke-width="3" stroke-dasharray="2.2 1.7"/>
    <circle cx="8" cy="8" r="3.6" fill="var(--blue)"/><circle cx="8" cy="8" r="1.5" fill="#fff"/>
  </svg>
  <div class="abs avatar" role="img" aria-label="Profile photo of the signed-in user"></div>
  <div class="abs greeting"><b>Hello</b><br>Tobin</div>

  <h2 class="abs section-title" style="left:132px;top:152px">You want</h2>
  <div class="tile" style="left:131px;top:189px;width:115px;height:57px;background:var(--mint)">Visual Arts<span class="remove">X</span></div>
  <div class="tile" style="left:247px;top:189px;width:140px;height:57px;background:var(--cyan)">Foreign Cinema<span class="remove">X</span></div>
  <div class="tile" style="left:131px;top:247px;width:130px;height:58px;background:var(--crimson)">Wine Tasting<span class="remove">X</span></div>
  <div class="tile" style="left:262px;top:247px;width:130px;height:58px;background:var(--sun)">Fine Dining<span class="remove">X</span></div>
  <div class="tile" style="left:131px;top:306px;width:108px;height:57px;background:var(--coral)">Musicals<span class="remove">X</span></div>

  <div class="abs date">Saturday, 14th of December</div>
  <div class="abs edit">Edit</div>
  <div class="abs time">6:00pm</div>
  <div class="abs city">London<small>(UK)</small></div>

  <div class="abs back">Back</div>

  <h2 class="abs section-title" style="left:428px;top:152px">Sites</h2>
  <h2 class="abs section-title" style="left:698px;top:152px">Events</h2>

  <!-- Sites -->
  <article class="card" style="left:428px;top:189px">
    <div class="body" style="background:var(--mint)"><h3>Veldra Modern</h3><p>Lorem ipsum dolor sit amet, consectetur adipiscing elit. Proin nec quam non ante...</p></div>
    <div class="photo photo-hall" role="img" aria-label="Photo of the gallery's vast turbine hall interior"></div>
    <div class="meta">Closes: 6 hours<svg width="14" height="12" viewBox="0 0 14 12"><path d="M7 12 L1 6 A3.2 3.2 0 0 1 7 2 A3.2 3.2 0 0 1 13 6 Z" fill="var(--heart)"/></svg></div>
  </article>
  <article class="card" style="left:428px;top:299px">
    <div class="body" style="background:var(--sky)"><h3>Corvane Museum<br>of Earth</h3><p>Lorem ipsum dolor sit amet, consectetur adipiscing elit. Proin nec quam non ante...</p></div>
    <div class="photo photo-museum" role="img" aria-label="Photo of the museum's grand hall with a skeleton display"></div>
    <div class="meta">Closes: 3 hours<svg width="14" height="12" viewBox="0 0 14 12"><path d="M7 12 L1 6 A3.2 3.2 0 0 1 7 2 A3.2 3.2 0 0 1 13 6 Z" fill="var(--heart)"/></svg></div>
  </article>
  <article class="card" style="left:428px;top:409px">
    <div class="body" style="background:var(--apricot)"><h3>Royal Ostwin Hall</h3><p>Lorem ipsum dolor sit amet, consectetur adipiscing elit. Proin nec quam non ante...</p></div>
    <div class="photo photo-dome" role="img" aria-label="Photo of the domed concert hall lit at dusk"></div>
    <div class="meta">Closes: 4 hours<svg width="14" height="12" viewBox="0 0 14 12"><path d="M7 12 L1 6 A3.2 3.2 0 0 1 7 2 A3.2 3.2 0 0 1 13 6 Z" fill="var(--heart)"/></svg></div>
  </article>
  <article class="card" style="left:428px;top:519px">
    <div class="body" style="background:var(--magenta)"><h3>Brennor Park</h3><p>Lorem ipsum dolor sit amet, consectetur adipiscing elit. Proin nec quam non ante...</p></div>
    <div class="photo photo-park" role="img" aria-label="Photo of bare trees along a park path"></div>
    <div class="meta">Closes: Never<svg width="14" height="12" viewBox="0 0 14 12"><path d="M7 12 L1 6 A3.2 3.2 0 0 1 7 2 A3.2 3.2 0 0 1 13 6 Z" fill="var(--heart)"/></svg></div>
  </article>

  <!-- Events -->
  <article class="card" style="left:698px;top:189px">
    <div class="body" style="background:var(--rose)"><h3>Veldra Modern</h3><p>Lorem ipsum dolor sit amet, consectetur adipiscing elit. Proin nec quam non ante...</p></div>
    <div class="photo photo-hall" role="img" aria-label="Photo of the gallery's vast turbine hall interior"></div>
    <div class="meta">Closes: 6 hours<svg width="14" height="12" viewBox="0 0 14 12"><path d="M7 12 L1 6 A3.2 3.2 0 0 1 7 2 A3.2 3.2 0 0 1 13 6 Z" fill="var(--heart)"/></svg></div>
  </article>
  <article class="card" style="left:698px;top:299px">
    <div class="body" style="background:var(--tangerine)"><h3>Corvane Museum<br>of Earth</h3><p>Lorem ipsum dolor sit amet, consectetur adipiscing elit. Proin nec quam non ante...</p></div>
    <div class="photo photo-museum" role="img" aria-label="Photo of the museum's grand hall with a skeleton display"></div>
    <div class="meta">Closes: 3 hours<svg width="14" height="12" viewBox="0 0 14 12"><path d="M7 12 L1 6 A3.2 3.2 0 0 1 7 2 A3.2 3.2 0 0 1 13 6 Z" fill="var(--heart)"/></svg></div>
  </article>
  <article class="card" style="left:698px;top:409px">
    <div class="body" style="background:var(--violet)"><h3>Royal Ostwin Hall</h3><p>Lorem ipsum dolor sit amet, consectetur adipiscing elit. Proin nec quam non ante...</p></div>
    <div class="photo photo-dome" role="img" aria-label="Photo of the domed concert hall lit at dusk"></div>
    <div class="meta">Closes: 4 hours<svg width="14" height="12" viewBox="0 0 14 12"><path d="M7 12 L1 6 A3.2 3.2 0 0 1 7 2 A3.2 3.2 0 0 1 13 6 Z" fill="var(--heart)"/></svg></div>
  </article>
  <article class="card" style="left:698px;top:519px">
    <div class="body" style="background:var(--lemon)"><h3>Brennor Park</h3><p>Lorem ipsum dolor sit amet, consectetur adipiscing elit. Proin nec quam non ante...</p></div>
    <div class="photo photo-park" role="img" aria-label="Photo of bare trees along a park path"></div>
    <div class="meta">Closes: Never<svg width="14" height="12" viewBox="0 0 14 12"><path d="M7 12 L1 6 A3.2 3.2 0 0 1 7 2 A3.2 3.2 0 0 1 13 6 Z" fill="var(--heart)"/></svg></div>
  </article>

  <div class="abs rail-cap"></div>
  <div class="abs rail"></div>
  <svg class="abs rail-arrow" width="12" height="24" viewBox="0 0 12 24" aria-label="More results">
    <path d="M0 0 L10 12 L0 24" fill="none" stroke="rgba(26,156,240,.45)" stroke-width="1.2"/>
  </svg>
</main>
</body>
</html>
```